Fairway Sunbelt Links Saver Pass

We need a design for a plastic rewards card that we would like to offer to our customers. The rewards card is for customers to show other golf courses to indicate that they get a discount at that participating course. Our Company name is "Fairway Sunbelt" the card is called the "Links Saver Pass" and our tag line is "Play More Pay Less". We would like the card to have an Australian feel and and use the colours Black and Yellow.

Target Market(s)

Golfers

Industry/Entity Type

Plastic

Requirements
Must have
• We have attached how our previous version looked with the detail that needs to be on the card. However the addresses on the front of the card needs to be removed and replaced with www.fairwaysunbelt-example.com.au. On the back of the card the address needs to be changed to "Fairway Sunbelt" P.O Box 4318, Coral Marsh W.A. Email: info@fairwaysunbelt-example.com.au

```html
<!DOCTYPE html>
<html lang="en">
<head>
<meta charset="utf-8">
<title>Fairway Sunbelt Links Saver Pass</title>
<link rel="stylesheet" href="https://fonts.googleapis.com/css2?family=Michroma&family=Open+Sans:wght@400;700&family=Arimo:wght@700&display=swap">
<style>
  :root {
    --bg: #e9e4dc;
    --card: #231f20;
    --card-edge: #3a3536;
    --yellow: #f5e51c;
    --grey-text: #c9c9c9;
    --white: #f2f2f2;
    --field: #e8e8e8;
    --orange: #e8902a;
    --green-light: #9fcf3c;
    --green-dark: #2f5a1c;
  }
  html, body {
    margin: 0;
    padding: 0;
    width: 1200px;
    height: 509px;
    overflow: hidden;
    background: var(--bg);
  }
  .canvas {
    position: relative;
    width: 1200px;
    height: 509px;
  }
  .card {
    position: absolute;
    width: 539px;
    height: 340px;
    background: var(--card);
    border: 1px solid var(--card-edge);
    box-sizing: border-box;
    overflow: hidden;
    font-family: "Open Sans", Verdana, sans-serif;
    color: var(--white);
  }
  .card-front { left: 48px; top: 80px; }
  .card-back { left: 612px; top: 83px; }

  /* Brand mark stand-in */
  .brand-mark {
    position: absolute;
    display: flex;
    align-items: center;
    gap: 8px;
  }
  .brand-mark .dot {
    width: 40px;
    height: 40px;
    border-radius: 50%;
    background: var(--orange);
    flex: none;
  }
  .brand-mark .name {
    font-family: "Open Sans", Verdana, sans-serif;
    font-weight: 700;
    font-size: 17px;
    color: var(--white);
    white-space: nowrap;
  }

  /* Front */
  .front-title {
    position: absolute;
    left: 26px;
    top: 20px;
    margin: 0;
    font-family: "Arimo", Arial, sans-serif;
    font-weight: 700;
    font-size: 28px;
    color: var(--yellow);
    letter-spacing: 0.3px;
  }
  .front-subtitle {
    position: absolute;
    left: 26px;
    top: 60px;
    margin: 0;
    font-family: "Michroma", sans-serif;
    font-size: 19px;
    font-weight: 400;
    color: var(--grey-text);
  }
  .front-brand { left: 345px; top: 28px; }
  .front-divider {
    position: absolute;
    left: 0;
    top: 98px;
    width: 100%;
    height: 4px;
    background: linear-gradient(90deg, #555 0%, #d8d8d8 45%, #9a9a9a 75%, #444 100%);
  }
  .tagline {
    position: absolute;
    right: 22px;
    top: 126px;
    margin: 0;
    font-family: "Michroma", sans-serif;
    font-size: 27px;
    color: var(--yellow);
    white-space: nowrap;
  }
  .course-photo {
    position: absolute;
    left: 0;
    top: 160px;
    width: 420px;
    height: 180px;
  }
  .website {
    position: absolute;
    right: 22px;
    bottom: 18px;
    margin: 0;
    font-family: "Open Sans", Verdana, sans-serif;
    font-size: 16px;
    color: var(--grey-text);
  }

  /* Back */
  .terms {
    position: absolute;
    left: 19px;
    top: 12px;
    width: 500px;
  }
  .section-label {
    margin: 0;
    font-weight: 700;
    font-size: 13.5px;
    color: var(--yellow);
  }
  .terms-list {
    list-style: none;
    margin: 1px 0 0;
    padding: 0;
    font-size: 13.5px;
    line-height: 15.5px;
  }
  .terms-list li {
    position: relative;
    padding-left: 19px;
  }
  .terms-list li::before {
    content: "";
    position: absolute;
    left: 2px;
    top: 5px;
    width: 6px;
    height: 6px;
    border-radius: 50%;
    background: var(--yellow);
  }
  .field {
    position: absolute;
    top: 120px;
  }
  .field-name { left: 19px; }
  .field-expiry { left: 321px; }
  .field-box {
    margin-top: 5px;
    height: 56px;
    background: var(--field);
    border: 1px solid #bdbdbd;
    box-sizing: border-box;
  }
  .field-name .field-box { width: 288px; }
  .field-expiry .field-box { width: 199px; }
  .contact-note {
    position: absolute;
    left: 19px;
    top: 211px;
    margin: 0;
    font-size: 13.5px;
    line-height: 16px;
  }
  .address {
    position: absolute;
    left: 28px;
    top: 260px;
    margin: 0;
    font-style: normal;
    font-size: 13.5px;
    line-height: 16px;
  }
  .address .company {
    font-weight: 700;
    color: var(--yellow);
  }
  .back-brand { left: 330px; top: 256px; }
</style>
</head>
<body>
<main class="canvas">

  <section class="card card-front" aria-label="Card front">
    <h1 class="front-title">Fairway Sunbelt</h1>
    <h2 class="front-subtitle">Links Saver Pass</h2>
    <div class="brand-mark front-brand">
      <span class="dot"></span>
      <span class="name">Fairway Sunbelt</span>
    </div>
    <div class="front-divider"></div>
    <p class="tagline">Play More Pay Less!</p>
    <svg class="course-photo" viewBox="0 0 420 180" role="img" aria-label="Photo of a sunlit golf fairway in a torn brush-edged shape, with a golf ball in the lower left corner">
      <defs>
        <linearGradient id="fairway-tone" x1="0" y1="0" x2="1" y2="1">
          <stop offset="0" stop-color="var(--green-dark)"/>
          <stop offset="0.45" stop-color="var(--green-light)"/>
          <stop offset="1" stop-color="var(--green-dark)"/>
        </linearGradient>
      </defs>
      <path d="M30 40 L120 18 L200 12 L300 8 L360 14 L400 10 L385 40 L405 70 L380 100 L395 130 L340 140 L300 150 L250 138 L200 150 L150 140 L120 160 L60 180 L0 180 L0 70 Z" fill="url(#fairway-tone)"/>
    </svg>
    <p class="website">www.fairwaysunbelt-example.com.au</p>
  </section>

  <section class="card card-back" aria-label="Card back">
    <div class="terms">
      <h3 class="section-label">Terms and Conditions</h3>
      <ul class="terms-list">
        <li>Cardholders must show their card to redeem offers at the participating outlets</li>
        <li>The Discounts apply to the card holder only.</li>
        <li>Golf course bookings are essential.</li>
        <li>The discounts available on the card are not valid with any other offer.</li>
      </ul>
    </div>
    <div class="field field-name">
      <h3 class="section-label">Card Holder Name</h3>
      <div class="field-box"></div>
    </div>
    <div class="field field-expiry">
      <h3 class="section-label">Expiry date</h3>
      <div class="field-box"></div>
    </div>
    <p class="contact-note">For information regarding this card contact:<br>The Administration Coordinator</p>
    <address class="address">
      <span class="company">Fairway Sunbelt</span><br>
      P.O Box 4318, Coral Marsh W.A.<br>
      Email: info@fairwaysunbelt-example.com.au
    </address>
    <div class="brand-mark back-brand">
      <span class="dot"></span>
      <span class="name">Fairway Sunbelt</span>
    </div>
  </section>

</main>
</body>
</html>
```